Design a Business Card

Business Name -- Crestwood Images

Owner’s name – Marlen Tuckett

Phone -- (555) 382-1074

Website – crestwoodimages.com

E-mail -- photographer@ crestwoodimages.com

Services -- Photography & Videography

Logo -- Image Attached

Self-picture -- Image Attached

Social Media Used – Friendlane, Pixora

You do not have to use the self-portrait that I included. You also do not have to include Owner’s Name, Social Media Used, or my E-mail address. Do what you think is best.

The business card should be 3.5” x 2”.

Use font-families that are included with an Adobe Photoshop subscription.

Retain layers so that I can edit the design later – I want the .PSD file.

Check that your design looks right when uploaded to Cardmill (https://cardmill.example/upload-design?mp_id=MP-918354&xnav=Business+Cards%3ACategory+Page_Category+Page_DesignFirst_tile-shell_0_ )

Please consider adding designs (either CC0 or basic things that you create on your own) to the card to make it more attractive.

Please create a design for both sides of the card, and use color on both sides.

```html
<!DOCTYPE html>
<html lang="en">
<head>
<meta charset="utf-8">
<title>Crestwood Images – Business Card</title>
<link rel="stylesheet" href="https://fonts.googleapis.com/css2?family=Roboto:wght@300;400;500;700&display=swap">
<style>
  :root {
    --page: #e4e6ea;
    --card-dark: #1f1c1d;
    --card-light: #ffffff;
    --accent: #2a8fd6;
    --text-light: #f2f2f2;
    --text-muted: #b9bcc2;
    --photo-deep: #1d2a3b;
    --photo-mid: #3c5674;
  }
  * { margin: 0; padding: 0; box-sizing: border-box; }
  html, body {
    width: 1200px; height: 900px; overflow: hidden;
    background: var(--page);
    font-family: "Roboto", Arial, sans-serif;
  }
  .sheet {
    position: relative; width: 1200px; height: 900px;
    display: flex; flex-direction: column; align-items: center; justify-content: center; gap: 60px;
  }
  .card {
    position: relative; width: 525px; height: 300px;
    border-radius: 18px; overflow: hidden;
    background: var(--card-dark);
    box-shadow: 0 8px 24px rgba(0,0,0,.18);
  }
  .card-art { position: absolute; inset: 0; }

  /* Brand lockup */
  .brand { position: absolute; display: flex; align-items: center; gap: 10px; }
  .brand-mark { width: 26px; height: 26px; border: 3px solid var(--accent); border-radius: 5px; }
  .brand-name { font-weight: 700; text-transform: uppercase; letter-spacing: .5px; font-size: 15px; }

  /* Front: logo + services */
  .card-front .brand { left: 22px; top: 134px; }
  .card-front .brand-name { color: #1f1c1d; font-size: 14px; }
  .services {
    position: absolute; left: 250px; right: 20px; top: 78px;
    text-align: center; color: var(--text-light);
  }
  .services-title { color: var(--accent); font-weight: 700; font-size: 24px; letter-spacing: 1px; margin-bottom: 18px; }
  .services-list { list-style: none; font-weight: 300; font-size: 20px; line-height: 1.45; letter-spacing: 1px; }

  /* Back: contact + portrait */
  .card-back .brand { left: 26px; top: 22px; }
  .card-back .brand-name { color: var(--text-light); }
  .owner { position: absolute; left: 26px; top: 70px; }
  .owner-name { color: var(--accent); font-weight: 700; font-size: 19px; text-transform: uppercase; letter-spacing: .5px; }
  .owner-role { color: var(--text-muted); font-size: 12px; margin-top: 2px; }
  .contact-list { position: absolute; left: 26px; top: 122px; list-style: none; }
  .contact-item { display: flex; align-items: center; gap: 8px; color: var(--text-light); font-size: 12px; height: 22px; }
  .contact-icon { width: 14px; height: 14px; flex: none; }
  .social-dot { width: 12px; height: 12px; border-radius: 50%; background: var(--accent); flex: none; }
</style>
</head>
<body>
<main class="sheet">

  <section class="card card-front" aria-label="Card front">
    <svg class="card-art" width="525" height="300" viewBox="0 0 525 300" aria-hidden="true">
      <path d="M0 0 H190 Q275 150 190 300 H0 Z" fill="var(--card-light)"/>
      <path d="M196 0 Q281 150 196 300" fill="none" stroke="var(--accent)" stroke-width="4"/>
    </svg>
    <div class="brand">
      <span class="brand-mark"></span>
      <span class="brand-name">Crestwood Images</span>
    </div>
    <div class="services">
      <h2 class="services-title">SERVICES :</h2>
      <ul class="services-list">
        <li>PHOTOGRAPHY</li>
        <li>&amp;</li>
        <li>VIDEOGRAPHY</li>
      </ul>
    </div>
  </section>

  <section class="card card-back" aria-label="Card back">
    <svg class="card-art" width="525" height="300" viewBox="0 0 525 300">
      <defs>
        <radialGradient id="portraitTone" cx="0.45" cy="0.35" r="0.7">
          <stop offset="0" stop-color="var(--photo-mid)"/>
          <stop offset="1" stop-color="var(--photo-deep)"/>
        </radialGradient>
      </defs>
      <circle cx="440" cy="340" r="228" fill="none" stroke="var(--accent)" stroke-width="4" aria-hidden="true"/>
      <circle cx="440" cy="340" r="220" fill="url(#portraitTone)" role="img" aria-label="Portrait of the photographer holding a camera"/>
    </svg>
    <div class="brand">
      <span class="brand-mark"></span>
      <span class="brand-name">Crestwood Images</span>
    </div>
    <div class="owner">
      <h1 class="owner-name">Marlen Tuckett</h1>
      <p class="owner-role">Owner</p>
    </div>
    <ul class="contact-list">
      <li class="contact-item">
        <svg class="contact-icon" viewBox="0 0 24 24" aria-hidden="true"><path fill="var(--accent)" d="M6.6 10.8a15.1 15.1 0 0 0 6.6 6.6l2.2-2.2c.3-.3.7-.4 1-.2 1.1.4 2.3.6 3.6.6.6 0 1 .4 1 1V20c0 .6-.4 1-1 1A17 17 0 0 1 3 4c0-.6.4-1 1-1h3.5c.6 0 1 .4 1 1 0 1.3.2 2.5.6 3.6.1.3 0 .7-.2 1z"/></svg>
        (555) 382-1074
      </li>
      <li class="contact-item">
        <svg class="contact-icon" viewBox="0 0 24 24" aria-hidden="true"><rect x="2" y="5" width="20" height="14" rx="2" fill="var(--accent)"/><path d="M3 6l9 7 9-7" fill="none" stroke="var(--card-dark)" stroke-width="2"/></svg>
        photographer@crestwoodimages.com
      </li>
      <li class="contact-item">
        <svg class="contact-icon" viewBox="0 0 24 24" aria-hidden="true"><circle cx="12" cy="12" r="9" fill="none" stroke="var(--accent)" stroke-width="2"/><ellipse cx="12" cy="12" rx="4" ry="9" fill="none" stroke="var(--accent)" stroke-width="2"/><path d="M3 12h18" stroke="var(--accent)" stroke-width="2"/></svg>
        www.crestwoodimages.com
      </li>
      <li class="contact-item">
        <span class="social-dot"></span>
        Friendlane · Pixora @crestwoodimages
      </li>
    </ul>
  </section>

</main>
</body>
</html>
```